Korvel Professional Services Website

Small website for company presence and information. Company is an IT/Telecom services company. We provide presales and installation services. Included are various company logos including color levels. Site doesn't have to use these exact colors in the logos, but should be complimentary if using different colors. It should have a professional business appearance.
Updates

My apologies for not being more responsive on the designs that have been submitted. I will be narrowing down the submissions and providing additional feedback next week. Thank you for your patience.

Project Deadline Extended
Reason: Sorry again for delays on picking designs. Work has me very busy and I've just not had the time to devote to this project. I am extending the design deadline for a few more days to give me time to make my final decisions. Thank you all for your patience. Stay tuned....

Target Market(s)

Telecom sales companies that sell Quenti telecom products.

Industry/Entity Type

Professional Service

Coding

Coded - Design and coding required

Number of Pages Required

5+ page

Font styles to use
Sans Serif

Colors
3276b5
0355a3
85abd2
85cae6
33a6d7
0692cd
ffffff

Requirements
Must have
• Professional design reflective of IT/Telecom business. A good reference website would be: http://www.lorbextech.example/. Looking for something similar in function and presence.
Nice to have
• Rolling photos highlighting our services. Traditional navigation across the top of all pages.
Should not have
• No motion video, flashy presentation or overly confused interface.

```html
<!DOCTYPE html>
<html lang="en">
<head>
<meta charset="utf-8">
<title>Korvel Professional Services</title>
<link href="https://fonts.googleapis.com/css2?family=Open+Sans:wght@400;600;700;800&display=swap" rel="stylesheet">
<style>
:root{
  --blue:#0692cd;
  --blue-light:#33a6d7;
  --blue-sky:#85cae6;
  --blue-mid:#3276b5;
  --navy:#0355a3;
  --ink:#1d2b3a;
  --text:#6b7682;
  --muted:#9aa4ae;
  --line:#e3e8ed;
  --panel:#f3f4f6;
  --white:#ffffff;
  --dark:#0e1a24;
}
*{box-sizing:border-box;margin:0;padding:0}
html,body{width:1200px;height:3688px;overflow:hidden}
body{font-family:"Open Sans",Arial,sans-serif;color:var(--text);background:var(--white);position:relative}
a{color:inherit;text-decoration:none}

/* header */
.site-header{position:absolute;top:0;left:0;width:1200px;height:112px;background:var(--white)}
.brand{position:absolute;left:136px;top:26px;display:flex;align-items:center;gap:14px}
.brand-mark{width:44px;height:44px;background:var(--navy)}
.brand-name{font-weight:700;font-size:20px;color:var(--navy);line-height:1.1;width:200px;text-transform:uppercase;letter-spacing:.5px}
.topbar-phone{position:absolute;right:136px;top:10px;height:26px;padding:0 14px;background:var(--navy);color:var(--white);font-size:12px;font-weight:600;display:flex;align-items:center;gap:8px;border-radius:2px}
.topbar-phone small{font-size:10px;font-weight:400;opacity:.8}
.main-nav{position:absolute;right:136px;top:48px;display:flex}
.main-nav a{display:block;height:64px;line-height:64px;padding:0 16px;font-size:12px;font-weight:600;color:var(--ink);text-transform:uppercase}
.main-nav a.active{background:var(--blue);color:var(--white)}

/* hero */
.hero{position:absolute;top:112px;left:0;width:1200px;height:508px;background:linear-gradient(90deg,#0b1620 0%,#1c2f3f 35%,#2d4c63 55%,#16283a 80%,#0a141d 100%)}
.hero-title{position:absolute;left:92px;top:225px;font-size:40px;font-weight:700;color:var(--white);line-height:1.15;text-transform:uppercase}
.btn{display:inline-flex;align-items:center;gap:8px;background:var(--blue);color:var(--white);font-size:12px;font-weight:700;text-transform:uppercase;height:38px;padding:0 20px}
.hero .btn{position:absolute;left:92px;top:318px}
.hero-dots{position:absolute;left:0;width:1200px;top:452px;display:flex;justify-content:center;gap:10px}
.hero-dots span{width:8px;height:8px;border-radius:50%;background:rgba(255,255,255,.45)}
.hero-dots span.on{background:var(--white)}

/* section heads */
.section-head{position:absolute;left:0;width:1200px;text-align:center}
.section-head h2{font-size:28px;font-weight:700;color:var(--navy);text-transform:uppercase}
.section-head .rule{width:60px;height:2px;background:var(--blue-sky);margin:12px auto 10px}
.section-head p{font-size:13px;color:var(--text)}

/* services */
.services{position:absolute;top:680px;left:0;width:1200px}
.service-grid{position:absolute;top:130px;left:160px;width:880px;display:grid;grid-template-columns:repeat(3,1fr);row-gap:72px}
.service{text-align:center}
.service svg{width:64px;height:64px;stroke:var(--blue);fill:none;stroke-width:2}
.service h3{margin-top:22px;font-size:14px;font-weight:700;color:var(--blue);text-transform:uppercase}
.service p{margin:12px auto 0;width:190px;font-size:11px;line-height:1.6;color:var(--text)}
.btn-outline{display:inline-block;margin-top:18px;border:1px solid var(--blue-sky);color:var(--blue);font-size:9px;font-weight:700;padding:6px 12px;text-transform:uppercase}

/* welcome band */
.welcome{position:absolute;top:1560px;left:0;width:1200px;height:560px;background:linear-gradient(180deg,var(--blue-light),var(--blue));clip-path:polygon(0 40px,100% 0,100% 520px,0 100%)}
.welcome-media{position:absolute;left:132px;top:104px;width:368px;height:336px;background:linear-gradient(135deg,#dfe9f2,#9fbfd8 55%,#4d7ea6)}
.play{position:absolute;left:160px;top:144px;width:48px;height:48px;border-radius:50%;background:#e0262a;display:flex;align-items:center;justify-content:center}
.welcome-copy{position:absolute;left:628px;top:228px;width:440px;color:var(--white)}
.welcome-copy h2{font-size:28px;font-weight:700;text-transform:uppercase}
.welcome-copy .lead{margin-top:18px;font-size:11px;font-weight:700;line-height:1.6}
.welcome-copy p{margin-top:12px;font-size:11px;line-height:1.7;opacity:.92}
.welcome-copy .btn{margin-top:22px;background:var(--navy)}

/* features */
.features{position:absolute;top:2120px;left:0;width:1200px;height:660px;background:var(--panel)}
.features .section-head{top:62px}
.feature-grid{position:absolute;top:228px;left:140px;width:920px;display:grid;grid-template-columns:repeat(3,1fr);row-gap:64px}
.feature{display:flex;gap:16px}
.feature svg{flex:none;width:34px;height:34px;stroke:var(--navy);fill:none;stroke-width:2}
.feature h3{font-size:13px;font-weight:700;color:var(--blue)}
.feature p{margin-top:8px;width:170px;font-size:11px;line-height:1.6}
.feature a{display:block;margin-top:12px;font-size:9px;font-weight:700;color:var(--blue);text-transform:uppercase}

/* installation */
.install{position:absolute;top:2780px;left:0;width:1200px;height:420px;background:linear-gradient(90deg,#6f6a66 0%,#b6aea6 40%,#d8d3cd 70%,#8a98aa 100%)}
.install-copy{position:absolute;left:128px;top:175px;color:var(--white)}
.install-copy h2{font-size:44px;font-weight:700;text-transform:uppercase}
.install-copy p{margin-top:10px;width:300px;font-size:13px;line-height:1.5}
.install-copy .btn{margin-top:22px}

/* footer */
.site-footer{position:absolute;top:3200px;left:0;width:1200px;height:488px;background:var(--white)}
.footer-brand{position:absolute;left:140px;top:104px}
.follow{position:absolute;left:248px;top:228px;text-align:center;font-size:11px;color:var(--text)}
.social{display:flex;gap:8px;margin-top:14px}
.social span{width:24px;height:24px;border-radius:50%;background:var(--blue-mid)}
.social span:nth-child(3){background:#d9563f}
.footer-col{position:absolute;top:124px}
.footer-col h4{font-size:12px;font-weight:700;color:var(--ink);text-transform:uppercase;margin-bottom:14px}
.footer-menu{left:688px}
.footer-menu li{list-style:none;font-size:11px;line-height:22px}
.footer-contact{left:900px}
.contact-row{display:flex;gap:12px;font-size:11px;line-height:1.5;margin-bottom:16px;width:180px}
.contact-row svg{flex:none;width:14px;height:14px;fill:var(--ink)}
.copyright{position:absolute;left:0;width:1200px;top:400px;border-top:1px solid var(--line);padding-top:18px;text-align:center;font-size:10px;color:var(--muted)}
</style>
</head>
<body>

<header class="site-header">
  <div class="brand"><span class="brand-mark"></span><span class="brand-name">Korvel Professional Services</span></div>
  <div class="topbar-phone"><small>CALL US</small>(555) 014-2290</div>
  <nav class="main-nav">
    <a class="active" href="#">Home</a><a href="#">About Us</a><a href="#">Services</a><a href="#">News &amp; Events</a><a href="#">Partners</a><a href="#">Contact Us</a>
  </nav>
</header>

<section class="hero" role="img" aria-label="Data centre aisle with rows of server racks lit in blue">
  <h1 class="hero-title">IT/Telecom<br>Services</h1>
  <a class="btn" href="#">Read More <span>›</span></a>
  <div class="hero-dots"><span class="on"></span><span></span><span></span><span></span><span></span></div>
</section>

<section class="services">
  <div class="section-head">
    <h2>Our Services</h2><div class="rule"></div>
    <p>Lorem Ipsum is simply dummy text of the printing and typesetting industry.</p>
  </div>
  <div class="service-grid">
    <div class="service">
      <svg viewBox="0 0 64 64"><rect x="8" y="42" width="8" height="14"/><rect x="22" y="34" width="8" height="22"/><rect x="36" y="24" width="8" height="32"/><rect x="50" y="12" width="8" height="44"/></svg>
      <h3>Presales</h3><p>It is a long established fact that a reader will be distracted by the readable content of a page.</p><a class="btn-outline" href="#">Read More</a>
    </div>
    <div class="service">
      <svg viewBox="0 0 64 64"><rect x="18" y="6" width="28" height="52" rx="3"/><circle cx="32" cy="28" r="8"/><path d="M32 16v4M32 36v4M20 28h4M40 28h4M26 50h12"/></svg>
      <h3>Installation</h3><p>It is a long established fact that a reader will be distracted by the readable content of a page.</p><a class="btn-outline" href="#">Read More</a>
    </div>
    <div class="service">
      <svg viewBox="0 0 64 64"><rect x="6" y="10" width="52" height="34" rx="2"/><path d="M24 54h16M32 44v10M22 26l6 6 12-12"/></svg>
      <h3>IT Services</h3><p>It is a long established fact that a reader will be distracted by the readable content of a page.</p><a class="btn-outline" href="#">Read More</a>
    </div>
    <div class="service">
      <svg viewBox="0 0 64 64"><path d="M14 8h12l4 12-7 5c3 7 9 13 16 16l5-7 12 4v12c0 3-3 6-6 6C26 56 8 38 8 14c0-3 3-6 6-6z"/><path d="M38 10c8 1 15 8 16 16M38 18c4 1 7 4 8 8"/></svg>
      <h3>Voice</h3><p>It is a long established fact that a reader will be distracted by the readable content of a page.</p><a class="btn-outline" href="#">Read More</a>
    </div>
    <div class="service">
      <svg viewBox="0 0 64 64"><circle cx="32" cy="32" r="8" fill="var(--blue)"/><circle cx="10" cy="10" r="5"/><circle cx="54" cy="10" r="5"/><circle cx="10" cy="54" r="5"/><circle cx="54" cy="54" r="5"/><path d="M14 14l12 12M50 14L38 26M14 50l12-12M50 50L38 38"/></svg>
      <h3>Network</h3><p>It is a long established fact that a reader will be distracted by the readable content of a page.</p><a class="btn-outline" href="#">Read More</a>
    </div>
    <div class="service">
      <svg viewBox="0 0 64 64"><rect x="10" y="8" width="44" height="14" rx="2"/><rect x="10" y="25" width="44" height="14" rx="2"/><rect x="10" y="42" width="44" height="14" rx="2"/><path d="M16 15h14M16 32h14M16 49h14M46 15h2M46 32h2M46 49h2"/></svg>
      <h3>Data Centres</h3><p>It is a long established fact that a reader will be distracted by the readable content of a page.</p><a class="btn-outline" href="#">Read More</a>
    </div>
  </div>
</section>

<section class="welcome">
  <div class="welcome-media" role="img" aria-label="Video still of a glowing globe surrounded by network connections"></div>
  <div class="play"><svg width="18" height="18" viewBox="0 0 18 18"><path d="M5 3l10 6-10 6z" fill="#fff"/></svg></div>
  <div class="welcome-copy">
    <h2>Welcome to Our Site</h2>
    <p class="lead">There are many variations of passages of Lorem Ipsum available, but the majority have suffered alteration.</p>
    <p>Many desktop publishing packages and web page editors now use Lorem Ipsum as their default model text, and a search for lorem ipsum will uncover many web sites still in their infancy. Various versions have evolved over the years, sometimes by accident, sometimes on purpose, and our team is here to help.</p>
    <a class="btn" href="#">Read More</a>
  </div>
</section>

<section class="features">
  <div class="section-head">
    <h2>Common Features</h2><div class="rule"></div>
    <p>Lorem Ipsum is simply dummy text of the printing</p>
  </div>
  <div class="feature-grid">
    <div class="feature"><svg viewBox="0 0 34 34"><rect x="7" y="15" width="20" height="15" rx="2"/><path d="M11 15v-5a6 6 0 0 1 12 0v5"/></svg><div><h3>Proactive Security</h3><p>It is a long established fact that a reader will be distracted.</p><a href="#">Read More ›</a></div></div>
    <div class="feature"><svg viewBox="0 0 34 34"><rect x="4" y="6" width="26" height="20" rx="2"/><path d="M9 21l6-6 4 4 7-8"/></svg><div><h3>Analytics</h3><p>It is a long established fact that a reader will be distracted.</p><a href="#">Read More ›</a></div></div>
    <div class="feature"><svg viewBox="0 0 34 34"><circle cx="17" cy="8" r="4"/><circle cx="7" cy="26" r="4"/><circle cx="27" cy="26" r="4"/><path d="M15 11l-6 12M19 11l6 12M11 26h12"/></svg><div><h3>Network</h3><p>It is a long established fact that a reader will be distracted.</p><a href="#">Read More ›</a></div></div>
    <div class="feature"><svg viewBox="0 0 34 34"><rect x="6" y="4" width="22" height="26" rx="2"/><path d="M11 11h12M11 17h12M11 23h8"/></svg><div><h3>Legacy</h3><p>It is a long established fact that a reader will be distracted.</p><a href="#">Read More ›</a></div></div>
    <div class="feature"><svg viewBox="0 0 34 34"><path d="M6 20v-4a11 11 0 0 1 22 0v4"/><rect x="4" y="19" width="6" height="9" rx="2"/><rect x="24" y="19" width="6" height="9" rx="2"/><path d="M27 28c0 3-4 4-8 4"/></svg><div><h3>Communications</h3><p>It is a long established fact that a reader will be distracted.</p><a href="#">Read More ›</a></div></div>
    <div class="feature"><svg viewBox="0 0 34 34"><circle cx="17" cy="10" r="6"/><path d="M5 32c0-7 5-12 12-12s12 5 12 12"/><path d="M17 20l-2 5 2 4 2-4z"/></svg><div><h3>Expert</h3><p>It is a long established fact that a reader will be distracted.</p><a href="#">Read More ›</a></div></div>
  </div>
</section>

<section class="install" role="img" aria-label="Technician's hand dialling on a desk telephone">
  <div class="install-copy">
    <h2>Installation</h2>
    <p>Contrary to popular belief, Lorem Ipsum is not simply random text. It has roots in a piece.</p>
    <a class="btn" href="#">Read More <span>›</span></a>
  </div>
</section>

<footer class="site-footer">
  <div class="brand footer-brand" style="position:absolute"><span class="brand-mark"></span><span class="brand-name">Korvel Professional Services</span></div>
  <div class="follow">FOLLOW US<div class="social"><span></span><span></span><span></span></div></div>
  <div class="footer-col footer-menu">
    <h4>Menu</h4>
    <ul><li>Home</li><li>About Us</li><li>Services</li><li>News &amp; Events</li><li>Partners</li><li>Contact Us</li></ul>
  </div>
  <div class="footer-col footer-contact">
    <h4>Contact Us</h4>
    <div class="contact-row"><svg viewBox="0 0 14 14"><path d="M7 0a5 5 0 0 0-5 5c0 4 5 9 5 9s5-5 5-9a5 5 0 0 0-5-5zm0 7a2 2 0 1 1 0-4 2 2 0 0 1 0 4z"/></svg><span>2150 Harlow Ridge Rd, Westbury, TX 75011</span></div>
    <div class="contact-row"><svg viewBox="0 0 14 14"><path d="M3 0h3l1 3-2 1.5c1 2 2.5 3.5 4.5 4.5L11 7l3 1v3c0 1.5-1 3-2.5 3C5 14 0 9 0 2.5 0 1 1.5 0 3 0z"/></svg><span>(555) 014-2290</span></div>
    <div class="contact-row"><svg viewBox="0 0 14 14"><path d="M0 2h14v10H0zM1 3l6 5 6-5v-.5H1z" fill-rule="evenodd"/></svg><span>info@korvelps.example</span></div>
  </div>
  <div class="copyright">Copyright © 2017 All Rights Reserved</div>
</footer>

</body>
</html>
```